Product Description page for Hullwrap.com, References here just need a clean up redesign

Hi, were working on updating the product description page of our site hullwrap.com

Attached is a reference of what we drew on paint. We want to keep it pretty much the same as far as whats on there, the components with a few small adjustments and a clean actually designed look.

1. We want to remove the tabs (product description, warranty, reviews) and put it all in that main content area stretching down into sections. IE: Product Description section, followed by reviews, followed by warranty, below each other.
2. The side bar needs to be redesigned as far as the look and feel but the content and whats in there should stay the same.
3. The main banner area will be replaced shortly you do not have to worry about that.
4. Include a section or box for people to put in their email for a free Ebook.

Target Market(s)

people looking to easily view our boat cover products and buy without having to click too often or leave the page.

Industry/Entity Type

Online Shopping

Number of Pages Required

1 page

Requirements
Must have
• - Must update the sidebar
• - Must update the content area to remove the tabs and put the content from each tab sectioned off below each other (dummy text is fine for now for the tabs you cant view)
Nice to have
• - Cool place thats clean and functional to insert a section for people to put in their email to receive a free ebook
Should not have
• - too much change, we already know what we want and have a solid reference to work from.

```html
<!DOCTYPE html>
<html lang="en">
<head>
<meta charset="utf-8">
<title>Hullwrap.com – Center Console Cover</title>
<link href="https://fonts.googleapis.com/css2?family=Roboto:wght@400;500;700&display=swap" rel="stylesheet">
<style>
:root{
  --blue:#1f63b0;
  --navy:#173a6c;
  --red:#d4262c;
  --ink:#333;
  --muted:#777;
  --line:#dde2e8;
  --soft:#f3f5f8;
}
*{box-sizing:border-box;margin:0;padding:0}
html,body{width:1200px;height:2428px;overflow:hidden}
body{font-family:"Roboto",Arial,sans-serif;color:var(--ink);background:#fff;font-size:13px;line-height:1.5;position:relative}
.header{height:56px;display:flex;align-items:center;justify-content:space-between;padding:0 60px}
.brand{font-weight:700;font-size:24px;color:var(--navy)}
.phone{display:flex;align-items:center;gap:8px;font-size:20px;font-weight:700;color:var(--blue)}
.phone .free{font-size:10px;background:var(--red);color:#fff;padding:2px 6px}
.nav{height:28px;background:var(--soft);border-top:1px solid var(--line);border-bottom:1px solid var(--line);display:flex;align-items:center;padding:0 60px}
.nav a{font-size:11px;color:var(--ink);text-decoration:none;padding:0 22px;border-right:1px solid var(--line);line-height:28px}
.nav .search{margin-left:auto;width:150px;height:18px;background:#fff;border:1px solid var(--line)}
.banner{height:48px;background:var(--blue);color:#fff;font-size:20px;font-weight:700;padding:0 60px;display:flex;align-items:center;margin-top:4px}
.wrap{position:absolute;left:60px;top:160px;width:1080px}
.crumbs{font-size:10px;color:var(--muted)}
.main{position:absolute;left:0;top:0;width:700px}
.side{position:absolute;left:712px;top:28px;width:368px}
h1.title{font-size:16px;font-weight:500;margin:10px 0 10px}
.photo{height:380px;background:linear-gradient(#f7f8fa,#e4e7ec);border:1px solid var(--line)}
.thumbs{display:flex;gap:8px;margin-top:14px}
.thumbs div{width:60px;height:36px;background:linear-gradient(#5d6f86,#2c3e56);border:1px solid var(--line)}
.thumbs div:first-child{background:linear-gradient(#eef0f3,#c9cfd7)}
.section{margin-top:34px}
.section h2{font-size:15px;font-weight:700;padding-bottom:6px;border-bottom:2px solid var(--line);margin-bottom:10px}
.section h3{font-size:10px;font-weight:700;color:var(--blue);text-transform:uppercase;margin:16px 0 4px}
.section p{font-size:10px;color:#555;margin-bottom:8px;line-height:1.7}
.section.tall p{margin-bottom:12px;line-height:1.9}
.section ul{font-size:10px;color:#555;list-style:none;line-height:1.7}
.specs{display:flex;gap:20px;margin-top:10px}
.specs div{flex:1;height:90px;background:linear-gradient(#4e5f75,#22344c)}
.review{border:1px solid var(--line);padding:12px;background:var(--soft)}
.stars{color:#f2a900;font-size:12px}
.scene{position:absolute;left:0;top:2220px;width:1200px;height:160px;background:linear-gradient(#9fc4e6,#6f95bb 55%,#3b5f86)}
.footbar{position:absolute;left:0;top:2380px;width:1200px;height:48px;background:var(--navy);color:#fff;font-size:11px;display:flex;align-items:center;padding:0 60px;gap:30px}
.box{border:1px solid var(--line);margin-bottom:20px}
.box .hd{background:var(--navy);color:#fff;font-size:11px;font-weight:500;padding:8px 12px}
.box .bd{padding:12px}
.price{display:flex;justify-content:space-between;align-items:baseline;border-bottom:1px solid var(--line);padding-bottom:8px}
.price b{font-size:15px;color:var(--red)}
.price span{font-size:12px;color:var(--blue);font-weight:500}
.rows{font-size:10px;color:var(--muted);margin:8px 0}
.rows div{display:flex;justify-content:space-between;line-height:1.9}
.btn{display:block;background:var(--navy);color:#fff;text-align:center;font-size:11px;font-weight:700;padding:8px;width:120px;margin-left:auto}
.sel{display:flex;gap:8px;align-items:center;font-size:10px;margin:6px 0}
.sel div{height:18px;border:1px solid var(--line);flex:1}
.ship{width:80px;height:80px;border-radius:50%;background:var(--blue);color:#fff;font-weight:700;font-size:13px;display:flex;align-items:center;justify-content:center;text-align:center;line-height:1.1;margin:0 0 20px 280px}
.item{display:flex;gap:10px;margin-bottom:12px;align-items:flex-start}
.item .img{width:70px;height:40px;background:linear-gradient(#56677d,#24364e);flex:none}
.item p{font-size:9px;color:#555;line-height:1.4}
.item p b{color:var(--blue);font-weight:500}
.item p em{font-style:normal;color:var(--red);font-weight:700}
.cover-img{height:70px;background:linear-gradient(#f1f3f6,#c5ccd6);margin-bottom:8px}
.note{font-size:9px;color:#555}
.deal{font-size:10px}
.deal s{color:#999}
.deal b{color:var(--red)}
.ebook label{font-size:11px;font-weight:700;color:var(--red);display:block}
.ebook p{font-size:9px;color:#555;margin:4px 0 8px}
.ebook .field{height:24px;border:1px solid var(--line);background:#fff;margin-bottom:8px}
.ebook .btn{margin:0;width:90px}
</style>
</head>
<body>
<header class="header">
  <div class="brand">Hullwrap.com</div>
  <div class="phone">
    <svg width="18" height="18" viewBox="0 0 24 24"><path fill="#1f63b0" d="M6.6 10.8a15 15 0 0 0 6.6 6.6l2.2-2.2c.3-.3.7-.4 1-.2 1.1.4 2.3.6 3.6.6.6 0 1 .4 1 1V20c0 .6-.4 1-1 1A17 17 0 0 1 3 4c0-.6.4-1 1-1h3.5c.6 0 1 .4 1 1 0 1.3.2 2.5.6 3.6.1.3 0 .7-.2 1z"/></svg>
    (800) 555-0142 <span class="free">FREE</span>
  </div>
</header>
<nav class="nav">
  <a>Boat Covers</a><a>Bass Boat Covers</a><a>T-Top Boat Covers</a><a>Model Pwc</a><a>Jet Ski Covers</a>
  <div class="search"></div>
</nav>
<div class="banner">up to 16'6" Long and 90" Wide</div>

<div class="wrap">
  <div class="main">
    <div class="crumbs">Home › Boat Covers › Center Console with Bow Rails › Up to 16'6" Long and 90" Wide</div>
    <h1 class="title">Fits Center Console with Bow Rails up to 16'6" Long and 90" Wide</h1>
    <div class="photo" role="img" aria-label="Boat wrapped in grey fitted cover on a trailer"></div>
    <div class="thumbs">
      <div role="img" aria-label="Covered boat thumbnail"></div><div role="img" aria-label="Fabric detail"></div><div role="img" aria-label="Strap detail"></div><div role="img" aria-label="Buckle detail"></div><div role="img" aria-label="Storage bag"></div><div role="img" aria-label="Hem detail"></div>
    </div>

    <section class="section">
      <h2>Product Info</h2>
      <h3>Description</h3>
      <p>This cover is tailored to fit center console boats with bow rails up to sixteen and a half feet long and ninety inches wide. The tough marine fabric blocks sun, rain and dust while letting trapped moisture escape, so your boat stays clean and dry between trips on the water.</p>
      <p>An elastic hem cord and adjustable straps keep the cover snug in transit and in storage. Reinforced seams and soft liners at the windshield points help prevent wear and protect your finish through every season of use.</p>
      <h3>Features</h3>
      <ul>
        <li>• Fits center console boats with bow rails</li>
        <li>• Heavy marine fabric with water repellent coating</li>
        <li>• Breathable weave resists mildew and fading</li>
        <li>• Elastic shock cord hem for a snug fit</li>
        <li>• Trailerable at highway speeds with straps</li>
        <li>• Double stitched seams for long lasting strength</li>
        <li>• Includes storage bag and tie down straps</li>
        <li>• Five year limited warranty included</li>
      </ul>
      <div class="specs">
        <div role="img" aria-label="Fabric close-up"></div><div role="img" aria-label="Strap system close-up"></div><div role="img" aria-label="Stitching close-up"></div><div role="img" aria-label="Vent close-up"></div>
      </div>
      <p style="margin-top:10px">Measure your boat from the tip of the bow to the back of the transom and around the widest point of the hull to confirm the right size before ordering this cover.</p>
    </section>

    <section class="section">
      <h2>Reviews</h2>
      <div class="review">
        <div class="stars">★★★★★ <span style="color:#555;font-size:10px">Dave</span></div>
        <p>"I bought this for my center console and it fits great. The fabric is thick and the straps hold it down well on the highway. Shipping was fast and the price was fair. I would order from here again."</p>
      </div>
    </section>

    <section class="section tall">
      <h2>Warranty</h2>
      <h3>Fit Guarantee</h3>
      <p>If your cover does not fit the boat sizes listed, contact us within thirty days and we will exchange it for the correct size at no extra cost. Please keep your receipt and the original packaging.</p>
      <p>Covers must be unused and returned in good condition. Our service team will walk you through the steps and send a prepaid label for the exchange.</p>
      <p>Exchanges are processed as soon as the returned cover reaches our warehouse, and the new size ships out the same business day.</p>
      <h3>Five Year Limited Warranty</h3>
      <p>Every cover is backed against defects in materials and workmanship for five years from purchase. This includes seams, fabric, straps and buckles under normal use and proper installation.</p>
      <p>Damage caused by wind whipping from loose straps, sharp edges or improper storage is not covered. Register your product online to speed up any future claim.</p>
      <h3>Return Policy</h3>
      <p>Items may be returned within thirty days for a refund of the purchase price. Return shipping is paid by the buyer unless the item arrived damaged or was sent in error.</p>
      <p>Refunds are issued to the original payment method within five business days after the returned item has been inspected by our team.</p>
      <h3>How To File A Claim</h3>
      <p>Call or email our service team with your order number and photos of the issue. We will review your claim and reply within two business days with next steps.</p>
    </section>

    <section class="section tall">
      <h2>Shipping</h2>
      <p>Orders placed before noon on business days ship the same day from our warehouse. Most orders arrive within three to five business days by ground service across the continental states.</p>
      <p>Free ground shipping is included on all covers. Expedited options are offered at checkout for an added fee. Tracking details are emailed as soon as your order leaves our dock.</p>
      <p>We ship to Alaska, Hawaii and most territories, though delivery times may be longer. International orders are reviewed by hand and a shipping quote is sent before payment is taken.</p>
      <p>Large orders for dealers and marinas can be shipped by freight. Contact our sales team for volume pricing and delivery scheduling.</p>
      <h3>Shipping Information</h3>
      <p>Please check your address before you submit your order. Packages returned due to an incorrect address will be reshipped once the correct details are confirmed by our team.</p>
    </section>
  </div>

  <aside class="side">
    <div class="box">
      <div class="hd">Deluxe Recreational Cover™</div>
      <div class="bd">
        <div class="price"><span>Our Price</span><b>$331.50</b></div>
        <div class="rows">
          <div><span>Regular Price</span><span>$390.00</span></div>
          <div><span>You Save</span><span>$58.50</span></div>
          <div><span>Item #</span><span>HW-1690</span></div>
        </div>
        <div class="sel">Color <div></div></div>
        <div class="sel">Qty <div style="flex:none;width:40px"></div></div>
        <span class="btn">ADD TO CART</span>
      </div>
    </div>
    <div class="ship">FREE<br>SHIPPING</div>
    <div class="box">
      <div class="hd">Frequently Purchased Together</div>
      <div class="bd">
        <div class="item"><div class="img" role="img" aria-label="Support pole"></div><p><b>Support Pole</b><br>Adjustable pole keeps water off the cover<br><em>$24.95</em></p></div>
        <div class="item"><div class="img" role="img" aria-label="Tie down straps"></div><p><b>Tie Down Straps</b><br>Extra straps for highway trailering<br><em>$14.95</em></p></div>
        <div class="item"><div class="img" role="img" aria-label="Vent kit"></div><p><b>Vent Kit</b><br>Reduces moisture under the cover<br><em>$19.95</em></p></div>
        <div class="item"><div class="img" role="img" aria-label="Motor cover"></div><p><b>Motor Cover</b><br>Shields your outboard from weather<br><em>$39.95</em></p></div>
        <div class="item"><div class="img" role="img" aria-label="Storage bag"></div><p><b>Storage Bag</b><br>Keeps your cover neat between uses<br><em>$12.95</em></p></div>
      </div>
    </div>
    <div class="box" style="margin-top:80px">
      <div class="hd">Looking for an adjustable cover?</div>
      <div class="bd">
        <div class="cover-img" role="img" aria-label="Boat under adjustable cover"></div>
        <p class="note">Universal fit cover with easy adjust straps for many boat styles</p>
        <p class="deal"><s>$239.00</s> <b>$189.75</b></p>
      </div>
    </div>
    <div class="box ebook">
      <div class="hd">Signup For Ebook</div>
      <div class="bd">
        <label>Free Ebook</label>
        <p>Boat care tips delivered to your inbox</p>
        <div class="field"></div>
        <span class="btn">SUBMIT</span>
      </div>
    </div>
  </aside>
</div>

<div class="scene" role="img" aria-label="Lake with boats and wooded shoreline"></div>
<footer class="footbar"><span>Sign Up for Email &amp; Save</span><span>(800) 555-0142</span><span style="margin-left:auto">© Hullwrap.com</span></footer>
</body>
</html>
```